Business Card Design For Office Furniture Clearance Company

Kestrel Office Clearance - our company name pretty much explains what we do, we clear offices for high end clients, mainly plc's and large international companies.

We require a nice looking business card that displays professionalism but without being too serious.

It would be nice to see just a little more than a conventional boring business card, make sure you add some flare.

Industry/Entity Type

Office Furniture

Contact Information for Business Card

CARD 1

Tom Pardew
Director
tom@kestrelofficeclearance.co.uk
m: 07700 513928

t: 01632 419063
www.kestrelofficeclearance.co.uk

Kestrel Office Clearance
Unit K4 B
3-7 Ferndale Lane
Ashcombe
Harrowfield
ZZ9 4QX

free office clearances… you cant get better than that.

CARD 2

Henry Walbrook
Director
henry@kestrelofficeclearance.co.uk
m: 07700 628157

t: 01632 419063

Kestrel Office Clearance
Unit K4 B
3-7 Ferndale Lane
Ashcombe
Harrowfield
ZZ9 4QX

Font styles to use
Sans Serif

Requirements
Must have
• A white background - as we have a blue logo.
Nice to have
• Nice use of the logo - play around with this and dissect it.

```html
<!DOCTYPE html>
<html lang="en">
<head>
<meta charset="utf-8">
<title>Kestrel Office Clearance – Business Cards</title>
<link href="https://fonts.googleapis.com/css2?family=Arimo:wght@400;700&display=swap" rel="stylesheet">
<style>
  :root {
    --bg: #eceef1;
    --card: #ffffff;
    --brand: #4d86c2;
    --brand-dark: #2f68a6;
    --brand-faint: #e6ecf6;
    --name: #86a5cc;
    --role: #8fb2df;
    --text: #4a4d52;
    --text-strong: #222428;
    --shadow: rgba(40, 50, 70, 0.16);
  }
  * { margin: 0; padding: 0; box-sizing: border-box; }
  html, body {
    width: 1200px; height: 720px; overflow: hidden;
    background: var(--bg);
    font-family: "Arimo", Arial, sans-serif;
  }
  .stage { position: relative; width: 1200px; height: 720px; }

  .card {
    position: absolute;
    width: 530px; height: 320px;
    background: var(--card);
    border-radius: 4px;
    box-shadow: 0 14px 30px var(--shadow), 0 2px 4px var(--shadow);
    overflow: hidden;
  }
  .card--front { left: 45px; top: 200px; }
  .card--back { left: 625px; top: 200px; }

  /* Front */
  .front-decor {
    position: absolute; right: -70px; top: -80px;
    width: 330px; height: 330px; border-radius: 50%;
    background: var(--brand-faint);
  }
  .front-brand {
    position: absolute; left: 34px; bottom: 38px;
    display: flex; flex-direction: column; align-items: flex-start; gap: 14px;
  }
  .brand-dot {
    width: 78px; height: 78px; border-radius: 50%;
    background: var(--brand);
  }
  .brand-name {
    font-weight: 700; color: var(--brand-dark);
    text-transform: uppercase; line-height: 1.05;
    letter-spacing: 0.01em;
  }
  .front-brand .brand-name { font-size: 21px; width: 170px; }

  .details {
    position: absolute; left: 230px; top: 36px;
  }
  .person-name {
    font-size: 21px; font-weight: 700; color: var(--name);
    text-transform: uppercase; letter-spacing: 0.01em;
  }
  .person-role { font-size: 15px; color: var(--role); margin-top: 2px; }
  .address {
    font-size: 13.5px; color: var(--text); line-height: 1.45;
    margin-top: 26px; font-style: normal;
  }
  .contacts { list-style: none; margin-top: 20px; }
  .contacts li {
    display: flex; align-items: center; gap: 10px;
    font-size: 13.5px; color: var(--text); line-height: 1; margin-bottom: 9px;
  }
  .contacts li.web { color: var(--text-strong); }
  .contact-icon { width: 14px; height: 14px; flex: none; }

  /* Back */
  .back-brand {
    position: absolute; inset: 0;
    display: flex; flex-direction: column; align-items: center; justify-content: center; gap: 20px;
  }
  .back-brand .brand-dot { width: 100px; height: 100px; }
  .back-brand .brand-name { font-size: 26px; }
</style>
</head>
<body>
<main class="stage">

  <section class="card card--front" aria-label="Business card front">
    <div class="front-decor"></div>

    <div class="front-brand">
      <div class="brand-dot"></div>
      <div class="brand-name">Kestrel Office Clearance</div>
    </div>

    <div class="details">
      <h1 class="person-name">Tom Pardew</h1>
      <p class="person-role">Director</p>
      <address class="address">
        Unit K4 B 3-7 Ferndale Lane<br>
        Ashcombe Harrowfield<br>
        ZZ9 4QX
      </address>
      <ul class="contacts">
        <li>
          <svg class="contact-icon" viewBox="0 0 14 14"><circle cx="7" cy="7" r="7" fill="var(--brand)"/><rect x="5" y="3.5" width="4" height="7" rx="0.8" fill="none" stroke="#fff" stroke-width="1"/></svg>
          07700 513928
        </li>
        <li>
          <svg class="contact-icon" viewBox="0 0 14 14"><circle cx="7" cy="7" r="7" fill="var(--brand)"/><path d="M4.5 4 L6 4 L6.6 5.6 L5.8 6.3 Q6.6 7.7 7.8 8.3 L8.5 7.5 L10 8.1 L10 9.6 Q6.5 10 4.4 5.6 Z" fill="#fff"/></svg>
          01632 419063
        </li>
        <li>
          <svg class="contact-icon" viewBox="0 0 14 14"><circle cx="7" cy="7" r="7" fill="var(--brand)"/><rect x="3.8" y="4.8" width="6.4" height="4.4" fill="none" stroke="#fff" stroke-width="0.9"/><path d="M3.8 4.8 L7 7.3 L10.2 4.8" fill="none" stroke="#fff" stroke-width="0.9"/></svg>
          tom@kestrelofficeclearance.co.uk
        </li>
        <li class="web">
          <svg class="contact-icon" viewBox="0 0 14 14"><circle cx="7" cy="7" r="7" fill="var(--brand)"/><circle cx="7" cy="7" r="3.3" fill="none" stroke="#fff" stroke-width="0.9"/><path d="M3.7 7 H10.3 M7 3.7 Q5.3 7 7 10.3 M7 3.7 Q8.7 7 7 10.3" fill="none" stroke="#fff" stroke-width="0.8"/></svg>
          www.kestrelofficeclearance.co.uk
        </li>
      </ul>
    </div>
  </section>

  <section class="card card--back" aria-label="Business card back">
    <div class="back-brand">
      <div class="brand-dot"></div>
      <div class="brand-name">Kestrel Office Clearance</div>
    </div>
  </section>

</main>
</body>
</html>
```